Bref créative
Business card/Letter head/Envelope for new staffing company
T & L Talent Partners
Professional
Dorian Wexley
41250 Orchard Pine, Suite 305
Warren, MI 48071
dwexley@tnlTalentPartners.com
www.tnlTalentPartners.com
GLSVC Certified
Would like color layout based on Logo but also want to be able to print letter head on laser printer so something that looks good in grey scale would be nice.
Need 'GLSVC Certified' to show somewhere on card, probably near bottom.
Do not need Company Name included since it is part of logo already.
Will upload AI format logo when available, waiting for designer to send in next day or so.
Color Logo
Black and White Logo
EPS Color Logo

```html
<!DOCTYPE html>
<html lang="en">
<head>
<meta charset="utf-8">
<title>T &amp; L Talent Partners — Stationery</title>
<link rel="stylesheet" href="https://fonts.googleapis.com/css2?family=Cinzel:wght@500;700&family=Open+Sans:wght@600;700&display=swap">
<style>
  :root{
    --stage:#000000;
    --paper:#ffffff;
    --navy:#1d3a6e;
    --blue:#0b6db3;
    --cyan:#1aa9d8;
    --grey:#8b8e93;
    --ink:#1e2a3a;
    --mono:#111111;
  }
  *{box-sizing:border-box;margin:0;padding:0}
  html,body{width:1200px;height:961px;overflow:hidden;background:var(--stage)}
  .stage{position:relative;width:1200px;height:961px}

  .card{position:absolute;width:421px;height:250px;background:var(--paper);overflow:hidden}
  .card--color{left:68px;top:148px}
  .card--mono{left:76px;top:486px;transform:rotate(8deg);transform-origin:center}
  .card svg.card-art{position:absolute;inset:0}

  .brand{position:absolute;display:flex;align-items:center;gap:8px;
    font-family:"Cinzel",serif;font-weight:700;color:var(--navy);line-height:1.05}
  .brand-mark{flex:none;background:var(--navy)}
  .card--mono .brand{color:var(--mono)}
  .card--mono .brand-mark{background:var(--mono)}
  .card .brand{left:24px;top:48px;width:120px;font-size:13px}
  .card .brand-mark{width:28px;height:28px}

  .holder{position:absolute;left:196px;top:26px;font-family:"Cinzel",serif;font-weight:500;
    font-size:22px;color:var(--blue);letter-spacing:.3px;white-space:nowrap}
  .contact{position:absolute;left:198px;top:60px;list-style:none;font-family:"Cinzel",serif;
    font-weight:700;font-size:8.5px;color:var(--ink);line-height:13px;white-space:nowrap}
  .contact li{display:flex;align-items:center;gap:5px}
  .contact svg{width:8px;height:8px;fill:var(--ink)}

  .card-web{position:absolute;left:16px;bottom:10px;font-family:"Open Sans",sans-serif;
    font-weight:700;font-size:10px;color:var(--paper)}
  .certified{position:absolute;left:296px;bottom:11px;font-family:"Cinzel",serif;
    font-weight:700;font-size:8px;color:var(--paper)}

  .letterhead{position:absolute;left:546px;top:112px;width:598px;height:759px;background:var(--paper);overflow:hidden}
  .letterhead svg.sheet-art{position:absolute;inset:0}
  .letterhead .brand{left:418px;top:49px;width:170px;font-size:15px}
  .letterhead .brand-mark{width:30px;height:30px}
  .rule{position:absolute;left:390px;right:0;height:4px}
  .rule--navy{top:126px;background:var(--navy)}
  .rule--cyan{top:135px;background:var(--cyan)}
  .sheet-web{position:absolute;right:14px;bottom:10px;font-family:"Open Sans",sans-serif;
    font-weight:700;font-size:10px;color:var(--paper)}
</style>
</head>
<body>
<main class="stage">

  <section class="card card--color">
    <svg class="card-art" viewBox="0 0 421 250" width="421" height="250" aria-hidden="true">
      <defs>
        <linearGradient id="bandA" x1="0" x2="1" y1="0" y2="0">
          <stop offset="0" stop-color="#1d3a6e"/><stop offset=".55" stop-color="#0b6db3"/><stop offset="1" stop-color="#1aa9d8"/>
        </linearGradient>
      </defs>
      <path d="M0,176 C130,150 280,178 421,146 L421,160 C280,194 130,166 0,190 Z" fill="#8b8e93"/>
      <path d="M0,198 C120,172 260,198 421,166 L421,250 L0,250 Z" fill="url(#bandA)"/>
      <path d="M0,198 C120,172 260,198 421,166" fill="none" stroke="#7fd3ef" stroke-width="2"/>
    </svg>
    <div class="brand"><span class="brand-mark"></span><span>T &amp; L Talent Partners</span></div>
    <h1 class="holder">Dorian Wexley</h1>
    <ul class="contact">
      <li>41250 Orchard Pine, Suite 305</li>
      <li>Warren, MI 48071</li>
      <li><svg viewBox="0 0 10 10"><path d="M2 0h2l1 3-1.5 1a6 6 0 0 0 2.5 2.5L7 5l3 1v2a2 2 0 0 1-2 2A8 8 0 0 1 0 2a2 2 0 0 1 2-2z"/></svg>555-201-0142</li>
      <li><svg viewBox="0 0 10 10"><rect x="1" y="2" width="8" height="6" rx="1"/></svg>555-201-0187</li>
      <li><svg viewBox="0 0 10 10"><path d="M0 2h10v6H0zM0 2l5 3.5L10 2" fill="none" stroke="#1e2a3a"/></svg>dwexley@tnlTalentPartners.com</li>
    </ul>
    <p class="certified">GLSVC Certified</p>
    <p class="card-web">www.tnlTalentPartners.com</p>
  </section>

  <section class="card card--mono">
    <svg class="card-art" viewBox="0 0 421 250" width="421" height="250" aria-hidden="true">
      <defs>
        <linearGradient id="bandB" x1="0" x2="1" y1="0" y2="0">
          <stop offset="0" stop-color="#1d3a6e"/><stop offset=".55" stop-color="#0b6db3"/><stop offset="1" stop-color="#1aa9d8"/>
        </linearGradient>
      </defs>
      <path d="M0,176 C130,150 280,178 421,146 L421,160 C280,194 130,166 0,190 Z" fill="#8b8e93"/>
      <path d="M0,198 C120,172 260,198 421,166 L421,250 L0,250 Z" fill="url(#bandB)"/>
      <path d="M0,198 C120,172 260,198 421,166" fill="none" stroke="#7fd3ef" stroke-width="2"/>
    </svg>
    <div class="brand"><span class="brand-mark"></span><span>T &amp; L Talent Partners</span></div>
    <h2 class="holder">Dorian Wexley</h2>
    <ul class="contact">
      <li>41250 Orchard Pine, Suite 305</li>
      <li>Warren, MI 48071</li>
      <li><svg viewBox="0 0 10 10"><path d="M2 0h2l1 3-1.5 1a6 6 0 0 0 2.5 2.5L7 5l3 1v2a2 2 0 0 1-2 2A8 8 0 0 1 0 2a2 2 0 0 1 2-2z"/></svg>555-201-0142</li>
      <li><svg viewBox="0 0 10 10"><rect x="1" y="2" width="8" height="6" rx="1"/></svg>555-201-0187</li>
      <li><svg viewBox="0 0 10 10"><path d="M0 2h10v6H0zM0 2l5 3.5L10 2" fill="none" stroke="#1e2a3a"/></svg>dwexley@tnlTalentPartners.com</li>
    </ul>
    <p class="certified">GLSVC Certified</p>
    <p class="card-web">www.tnlTalentPartners.com</p>
  </section>

  <section class="letterhead">
    <svg class="sheet-art" viewBox="0 0 598 759" width="598" height="759" aria-hidden="true">
      <defs>
        <linearGradient id="sheetBand" x1="0" x2="1" y1="0" y2="1">
          <stop offset="0" stop-color="#1aa9d8"/><stop offset=".5" stop-color="#0b6db3"/><stop offset="1" stop-color="#1d3a6e"/>
        </linearGradient>
      </defs>
      <rect width="598" height="759" fill="url(#sheetBand)"/>
      <path d="M0,80 C40,25 180,4 370,0 L598,0 L598,500 C580,670 440,735 200,759 L0,759 Z" fill="#ffffff"/>
      <path d="M0,80 C40,25 180,4 370,0" fill="none" stroke="#7fd3ef" stroke-width="3"/>
      <path d="M598,500 C580,670 440,735 200,759" fill="none" stroke="#7fd3ef" stroke-width="3"/>
    </svg>
    <div class="brand"><span class="brand-mark"></span><span>T &amp; L Talent Partners</span></div>
    <span class="rule rule--navy"></span>
    <span class="rule rule--cyan"></span>
    <p class="sheet-web">www.tnlTalentPartners.com</p>
  </section>

</main>
</body>
</html>
```